New business card for UK roofing company

We are Brindmore Roofing and we need a business card design for our staff.

We offer the following services:

- New roofs
- General roof repairs
- Drone surveys
- Single ply roofing
- Steel cladding
- Asbestos removal
- Electronic leak detection

I have attached our logo. I have also attached example branding printed to our vans. The business card should fit in with the style of our branding.

The business card should have the following information;

Address:
Unit 17c Wendlecroft Farm
Wendlecroft Lane
Hatchington
CM4 9QD

Telephone: 020 7946 0372
24 Hour: 0800 612 4479

Email: ray@brindmoreroofing.example
Mobile: 07700981234
Name: Ray Tunstead
Website: www.brindmoreroofing.example

The business card will be printed in Spot UV, see here: https://www.kestaprint.example/business-cards/spot-uv/

If you need anymore info, please let me know,

```html
<!DOCTYPE html>
<html lang="en">
<head>
<meta charset="utf-8">
<title>Brindmore Roofing – Business Card</title>
<link rel="stylesheet" href="https://fonts.googleapis.com/css2?family=Poppins:wght@600&family=Roboto:wght@400&display=swap">
<style>
  :root {
    --backdrop: #2b2b2c;
    --card-blue: #1f4571;
    --card-blue-deep: #1b3d66;
    --emboss-blue: #35618f;
    --accent: #2aa3d8;
    --text-light: #e7e9ee;
  }
  * { margin: 0; padding: 0; box-sizing: border-box; }
  html, body {
    width: 1200px; height: 1138px; overflow: hidden;
    background: var(--backdrop);
    font-family: "Roboto", Arial, sans-serif;
  }
  .card {
    position: absolute; left: 290px;
    width: 620px; height: 376px;
    border-radius: 16px;
    background: linear-gradient(180deg, var(--card-blue) 0%, var(--card-blue-deep) 100%);
    color: var(--text-light);
  }
  .card--front { top: 184px; }
  .card--back { top: 606px; }

  .front-brand {
    position: absolute; left: 0; right: 0; top: 150px;
    text-align: center;
    font-family: "Poppins", Arial, sans-serif; font-weight: 600;
    font-size: 50px; color: var(--emboss-blue);
  }
  .tagline {
    position: absolute; left: 0; right: 0; top: 330px;
    text-align: center; font-size: 15px;
  }
  .accent { color: var(--accent); }

  .person-name {
    position: absolute; left: 34px; top: 52px;
    font-family: "Poppins", Arial, sans-serif; font-weight: 600;
    font-size: 25px;
  }
  .brand-mark {
    position: absolute; right: 32px; top: 150px;
    display: flex; align-items: center; gap: 12px;
  }
  .brand-dot {
    width: 26px; height: 26px; border-radius: 50%;
    background: var(--accent);
  }
  .brand-name {
    font-family: "Poppins", Arial, sans-serif; font-weight: 600;
    font-size: 30px; color: var(--accent); line-height: 1;
  }

  .contact-list {
    position: absolute; left: 34px; top: 244px;
    list-style: none; font-size: 16px; line-height: 24px;
  }
  .contact-list li { display: flex; align-items: center; gap: 12px; }
  .contact-list svg { width: 16px; height: 16px; fill: var(--accent); flex: none; }

  .address {
    position: absolute; right: 32px; top: 244px;
    font-style: normal; text-align: right;
    font-size: 16px; line-height: 24px;
  }
  .phone-line {
    position: absolute; left: 0; right: 0; top: 323px;
    text-align: center; font-size: 16px;
  }
</style>
</head>
<body>

<section class="card card--front">
  <div class="front-brand">Brindmore Roofing</div>
  <p class="tagline"><span class="accent">Commercial</span> &amp; <span class="accent">Residential Roofing</span> Services.</p>
</section>

<section class="card card--back">
  <h1 class="person-name">Ray Tunstead</h1>

  <div class="brand-mark">
    <span class="brand-dot"></span>
    <span class="brand-name">Brindmore Roofing</span>
  </div>

  <ul class="contact-list">
    <li>
      <svg viewBox="0 0 16 16" aria-hidden="true"><path d="M1 5c0-2 3-3 7-3s7 1 7 3v1h-3V5H4v1H1zM4 7h8l2 7H2z"/><circle cx="8" cy="10.5" r="1.8" fill="#1f4571"/></svg>
      <span>07700981234</span>
    </li>
    <li>
      <svg viewBox="0 0 16 16" aria-hidden="true"><path d="M1 3h14v10H1z"/><path d="M1.5 3.5 8 9l6.5-5.5" fill="none" stroke="#1f4571" stroke-width="1.4"/></svg>
      <span>ray@brindmoreroofing.example</span>
    </li>
    <li>
      <svg viewBox="0 0 16 16" aria-hidden="true"><circle cx="8" cy="8" r="7"/><path d="M1 8h14M8 1c-3 3-3 11 0 14M8 1c3 3 3 11 0 14" fill="none" stroke="#1f4571" stroke-width="1"/></svg>
      <span>www.brindmoreroofing.example</span>
    </li>
  </ul>

  <address class="address">
    Unit 17c Wendlecroft Farm<br>
    Wendlecroft Lane<br>
    Hatchington, Marlbury CM4 9QD
  </address>

  <p class="phone-line"><span class="accent">Telephone:</span> 020 7946 0372 <span class="accent">24 Hour:</span> 0800 612 4479</p>
</section>

</body>
</html>
```